Wedding expo flyer design

My name is Dorian Whitcombe and my business is called vowsbyharlow and I am a celebrant who is based in Perth Western Australia.
I am exhibiting at an expo at Gilded Arena in September and this is a DL flyer with entry details for a competition. I want my details on it for the customer to keep and the other half is the entry return with their contact details.
By filling in your details and placing this entry form in the competition box at Dorian's booth you could win.
The first prize is a $700.00 travel voucher from Vowsbyharlow and Skylark Voyages Denholm, second Prize is 2a free wedding to the value of $600.00 and third prize is 2 bottles of Varenne et Baudry Champagne.
I would like to see a modern bridal design with colours hot pink, gold and white.

Target Market(s)

22-35 year olds

Industry/Entity Type

Wedding

Logo Text

Vowsbyharlow ebridal competition

Logo styles of interest
Pictorial/Combination Logo
Requirements
Must have
• Dorian Whitcombe is a vibrant and competent local Perth celebrant (B47286) who has performed over 70 individualized weddings, commitment ceremonies, renewal of vows, funerals and naming ceremonies in and around Perth and the South West of WA and even as far away as the Isle of Pines in the South Pacific.
By booking Dorian now you will ensure a 10% discount and have a ceremony to remember.
Contact Dorian on m. 0491625803 e. dorian@vowsbyharlow.example w.www.vowsbyharlow.example p. PO Box 318 Larkfield Rise 6082 WA.

```html
<!DOCTYPE html>
<html lang="en">
<head>
<meta charset="utf-8">
<title>Vowsbyharlow – Expo Flyer</title>
<link rel="stylesheet" href="https://fonts.googleapis.com/css2?family=Fira+Sans:ital,wght@0,300;0,400;0,600;1,400;1,600&display=swap">
<style>
  :root {
    --hot-pink: #f47bb5;
    --blush: #f9bcd9;
    --label-pink: #f05fa3;
    --gold: #de9a1e;
    --rule-gold: #d9a53c;
    --ink: #2a2a2a;
    --muted: #555555;
    --white: #ffffff;
    --cream: #fbf1df;
    --dash: #f27ab3;
  }
  * { margin: 0; padding: 0; box-sizing: border-box; }
  html, body { width: 1200px; height: 2607px; overflow: hidden; background: var(--white); }
  body { font-family: "Fira Sans", sans-serif; color: var(--ink); }
  .flyer { position: relative; width: 1200px; height: 2607px; overflow: hidden; background: var(--white); }
  .backdrop { position: absolute; left: 0; top: 0; width: 1200px; height: 2607px; }
  .brand-name {
    position: absolute; left: 420px; top: 150px;
    font-weight: 300; font-size: 112px; line-height: 1; color: var(--white); letter-spacing: 1px;
  }
  .intro, .offer {
    position: absolute; left: 124px; font-size: 35px; line-height: 52.5px; color: var(--ink); font-weight: 300;
  }
  .intro { top: 340px; }
  .offer { top: 888px; }
  .contact { position: absolute; left: 537px; top: 985px; }
  .contact-name { font-size: 41px; font-weight: 600; color: var(--gold); line-height: 52px; }
  .contact-role { font-size: 31px; font-style: italic; color: var(--muted); line-height: 44px; margin-bottom: 28px; }
  .contact-list { list-style: none; font-size: 32px; line-height: 52px; color: var(--muted); font-weight: 300; }
  .contact-list li { display: flex; }
  .contact-list .key { color: var(--label-pink); font-weight: 600; width: 34px; flex: none; }
  .cut-line { position: absolute; left: 0; top: 1486px; width: 1200px; border-top: 3px dashed var(--dash); }
  .entry { position: absolute; left: 128px; top: 1508px; width: 960px; }
  .entry-title { font-size: 42px; font-weight: 600; font-style: italic; color: var(--gold); line-height: 60px; margin-bottom: 12px; }
  .entry-intro, .prize { font-size: 32px; line-height: 52px; font-weight: 300; color: var(--ink); }
  .entry-intro { margin-bottom: 18px; }
  .prize { margin-bottom: 26px; }
  .prize .rank { color: var(--label-pink); font-weight: 600; }
  .entry-form { position: absolute; left: 128px; top: 1955px; width: 958px; }
  .field { height: 74px; border-bottom: 3px solid var(--rule-gold); font-size: 31px; font-weight: 300; color: var(--ink); display: flex; align-items: flex-end; padding-bottom: 2px; }
  .field.first { height: 52px; }
</style>
</head>
<body>
<main class="flyer">
  <svg class="backdrop" viewBox="0 0 1200 2607" xmlns="http://www.w3.org/2000/svg">
    <defs>
      <linearGradient id="bride-tone" x1="0" y1="0" x2="0" y2="1">
        <stop offset="0" stop-color="#2b2226"/>
        <stop offset="0.55" stop-color="#6d5a63"/>
        <stop offset="1" stop-color="#ffffff"/>
      </linearGradient>
      <linearGradient id="flourish-tone" x1="0" y1="0" x2="1" y2="0">
        <stop offset="0" stop-color="#fbead2"/>
        <stop offset="1" stop-color="#ffffff"/>
      </linearGradient>
    </defs>
    <rect class="form-pattern" x="0" y="1495" width="820" height="1112" fill="url(#flourish-tone)" role="img" aria-label="Faint cream damask flourish pattern behind the entry form"/>
    <path class="pink-field" fill="var(--hot-pink)" d="M0,0 H1200 V800 C1000,805 800,840 640,920 C520,980 430,1060 360,1190 C290,1320 240,1450 190,1600 C120,1800 50,1950 0,2070 Z"/>
    <path class="veil-sweep" fill="var(--blush)" d="M780,470 C560,800 300,1250 0,1650 L0,2070 C50,1950 120,1800 190,1600 C240,1450 290,1320 360,1190 C430,1060 520,980 640,920 C700,880 750,800 780,470 Z"/>
    <rect class="corner-flourish" x="0" y="0" width="330" height="225" rx="0" fill="#3a2a31" role="img" aria-label="Black swirling floral flourish in the top corner"/>
    <rect class="bride-figure" x="770" y="470" width="240" height="360" rx="40" fill="url(#bride-tone)" role="img" aria-label="Silhouette illustration of a bride in a strapless white gown holding a yellow and white bouquet"/>
  </svg>

  <div class="brand-name">Vowsbyharlow</div>

  <p class="intro">
    Dorian Whitcombe is a vibrant and<br>
    competent local Perth celebrant<br>
    (B47286) who has performed over<br>
    70 individualized weddings,<br>
    commitment ceremonies, renewal<br>
    of vows, funerals and naming<br>
    ceremonies in and around Perth<br>
    and the South West of WA and<br>
    even as far away as the Isle of<br>
    Pines in the South Pacific.
  </p>

  <p class="offer">
    By booking Dorian<br>
    now you will ensure<br>
    a 10% discount<br>
    and have a<br>
    ceremony to<br>
    remember.
  </p>

  <section class="contact">
    <h2 class="contact-name">Dorian Whitcombe</h2>
    <p class="contact-role">Marriage Celebrant</p>
    <ul class="contact-list">
      <li><span class="key">m.</span><span>0491 625 803</span></li>
      <li><span class="key">e.</span><span>dorian@vowsbyharlow.example</span></li>
      <li><span class="key">w.</span><span>www.vowsbyharlow.example</span></li>
      <li><span class="key">p.</span><span>PO Box 318<br>Larkfield Rise<br>WA 6082</span></li>
    </ul>
  </section>

  <div class="cut-line"></div>

  <section class="entry">
    <h2 class="entry-title">Fill in to win!</h2>
    <p class="entry-intro">By filling in your details and placing this entry form in the competition box at Dorian’s booth you could win:</p>
    <p class="prize"><span class="rank">FIRST PRIZE:</span> $700 travel voucher from Vowsbyharlow and Skylark Voyages Denholm</p>
    <p class="prize"><span class="rank">SECOND PRIZE:</span> free wedding to the value of $600</p>
    <p class="prize"><span class="rank">THIRD PRIZE:</span> 2 bottles of Varenne et Baudry Champagne.</p>
  </section>

  <div class="entry-form">
    <div class="field first">Name</div>
    <div class="field" style="height:108px">Address</div>
    <div class="field"></div>
    <div class="field"></div>
    <div class="field">email</div>
    <div class="field">phone</div>
  </div>
</main>
</body>
</html>
```